"Tidewell Fellowship" needs a logo design that represents a Christian family boating ministry

Mission Statement:
“Providing compassion, care and opportunities to create memories for marginalized groups of society through ocean therapy.”
Bible verse:
Colossians 3:12 – “Therefore, as God’s chosen people, holy and dearly loved, clothe yourselves with compassion, kindness, humility, gentleness and patience.”
Target Market(s)
HOMELESS (who have gone through shelters and are on the road to recovery)
CHURCH GROUPS
INJURED MILITARY VETERANS
YOUTH AT RISK (orphans, human trafficking survivors)
SICKLY (hospitalized who can get out once in a while)
CAREGIVERS (single moms, military spouses caring for injured vets, families of those in prison)
ELDERLY (retirement centers)
SMALL BUSINESS STAFF OUTINGS
SPECIAL EVENTS
Industry/Entity Type
Ministry
Contact Information for Business Card
Captain Glen Marlowe @ 808-491-3027
Priscilla Marlowe @ 808-493-5184
info@tidewellfellowship.example
www.tidewellfellowship.example (not active yet but hopefully, soon)
Requirements
Must have
- Catch-phrase words maybe for back of business card:
- "Tide-Bound --- Kindness --- Making moments out at sea"
Nice to have
- Added 2 photo files just for visuals:
- 1 photo is of our boat.
- Other photo is our daughter's artwork on a cooler she made (for father's day gift)...might be nice and fun to incorporate daughter's artwork/inspiration into logo...but not sure if it looks to busy

```html
<!DOCTYPE html>
<html lang="en">
<head>
<meta charset="utf-8">
<title>Tidewell Fellowship – Business Card</title>
<link rel="stylesheet" href="https://fonts.googleapis.com/css2?family=Arimo:wght@400&family=Tinos:wght@400;700&display=swap">
<style>
  :root {
    --indigo: #34308f;
    --indigo-deep: #2b2a86;
    --glow: #e8793a;
    --sky: #1cb0ea;
    --orange: #f28a1e;
    --ink: #1d1d1f;
    --paper: #ffffff;
    --backdrop: #e9e6e1;
  }
  * { box-sizing: border-box; margin: 0; padding: 0; }
  html, body { width: 900px; height: 1200px; overflow: hidden; }
  body { background: var(--backdrop); position: relative; font-family: "Tinos", "Times New Roman", serif; }

  .card {
    position: absolute;
    width: 734px;
    height: 429px;
    border-radius: 24px;
    background: var(--paper);
    overflow: hidden;
    box-shadow: 0 6px 16px rgba(0,0,0,.25);
  }
  .card--front { left: 88px; top: 133px; }
  .card--back { left: 82px; top: 630px; }

  /* front header */
  .header-band {
    position: absolute; left: 0; top: 0; width: 100%; height: 225px;
    background:
      radial-gradient(ellipse 230px 150px at 50% 100%, rgba(232,121,58,.95) 0%, rgba(170,80,110,.55) 45%, rgba(52,48,143,0) 100%),
      var(--indigo);
  }
  .accent-stripe {
    position: absolute; left: 0; top: 229px; width: 100%; height: 12px;
    background: var(--sky);
  }

  .brand {
    position: absolute;
    display: flex; align-items: center; gap: 22px;
  }
  .brand__dot { width: 74px; height: 74px; border-radius: 50%; background: var(--orange); flex: none; }
  .brand__name {
    font-family: "Tinos", "Times New Roman", serif;
    font-weight: 400;
    font-size: 50px;
    letter-spacing: 1px;
    white-space: nowrap;
  }
  .card--front .brand { left: 95px; top: 72px; }
  .card--front .brand__name { color: var(--paper); }
  .card--back .brand { left: 100px; top: 152px; }
  .card--back .brand__name { color: var(--ink); }

  /* contacts */
  .contact {
    position: absolute; top: 300px;
    font-size: 17px; color: var(--ink);
  }
  .contact__name { font-weight: 700; font-size: 20px; margin-bottom: 6px; }
  .contact__phone { display: flex; align-items: center; gap: 9px; }
  .contact__phone svg { width: 20px; height: 16px; flex: none; }
  .contact--left { left: 38px; }
  .contact--right { right: 40px; text-align: right; }
  .contact--right .contact__name { text-align: right; }
  .contact--right .contact__phone { justify-content: flex-end; }

  .contact-rule {
    position: absolute; left: 38px; right: 40px; top: 359px;
    height: 2px; background: var(--ink);
  }
  .web-line {
    position: absolute; left: 38px; right: 40px; top: 368px;
    display: flex; justify-content: space-between;
    font-size: 17px; color: var(--ink);
  }

  /* back */
  .tagline-band {
    position: absolute; left: 0; bottom: 0; width: 100%; height: 67px;
    background: var(--indigo-deep);
    display: flex; align-items: center; justify-content: center; gap: 10px;
    font-family: "Arimo", Arial, sans-serif; font-size: 18.5px; color: var(--paper);
  }
  .tagline-band .sep { width: 8px; height: 8px; border-radius: 50%; background: var(--orange); }
</style>
</head>
<body>

<section class="card card--front" aria-label="Business card front">
  <div class="header-band"></div>
  <div class="accent-stripe"></div>
  <div class="brand">
    <span class="brand__dot"></span>
    <span class="brand__name">Tidewell Fellowship</span>
  </div>

  <div class="contact contact--left">
    <p class="contact__name">Priscilla Marlowe</p>
    <p class="contact__phone">
      <svg viewBox="0 0 20 16" aria-hidden="true"><path fill="#1cb0ea" d="M2 5c0-2 3-3 8-3s8 1 8 3v1.5h-4V5H6v1.5H2z M5 8h10l2 6H3z"/><circle cx="10" cy="11" r="1.8" fill="#fff"/></svg>
      808-493-5184
    </p>
  </div>
  <div class="contact contact--right">
    <p class="contact__name">Captain Glen Marlowe</p>
    <p class="contact__phone">
      808-491-3027
      <svg viewBox="0 0 20 16" aria-hidden="true"><path fill="#1cb0ea" d="M2 5c0-2 3-3 8-3s8 1 8 3v1.5h-4V5H6v1.5H2z M5 8h10l2 6H3z"/><circle cx="10" cy="11" r="1.8" fill="#fff"/></svg>
    </p>
  </div>
  <div class="contact-rule"></div>
  <div class="web-line">
    <span>info@tidewellfellowship.example</span>
    <span>www.tidewellfellowship.example</span>
  </div>
</section>

<section class="card card--back" aria-label="Business card back">
  <div class="brand">
    <span class="brand__dot"></span>
    <span class="brand__name">Tidewell Fellowship</span>
  </div>
  <div class="tagline-band">
    <span>Tide-Bound</span><span class="sep"></span>
    <span>Kindness</span><span class="sep"></span>
    <span>Making moments out at sea</span>
  </div>
</section>

</body>
</html>
```